Commercial facility maintenance

I need a card design that helps my salesmen make contact with new clients, our product is facility maintenance and heavy industrial maintenance

```html
<!DOCTYPE html>
<html lang="en">
<head>
<meta charset="utf-8">
<title>Harlow Ironworks – Business Card</title>
<link href="https://fonts.googleapis.com/css2?family=Space+Grotesk:wght@400;600;700&display=swap" rel="stylesheet">
<style>
  :root {
    --stage: #8e8e8e;
    --card-dark: #262627;
    --card-light: #ffffff;
    --ink-dark: #3b3b3d;
    --ink-muted: #58585a;
    --ink-faint: #3e3e40;
    --brand-red: #9b2226;
    --rule-dark: #38383a;
    --rule-light: #8a8a8a;
    --watermark: #f1f1f1;
  }
  * { margin: 0; padding: 0; box-sizing: border-box; }
  html, body { width: 1200px; height: 1000px; overflow: hidden; }
  body {
    background: var(--stage);
    font-family: "Space Grotesk", sans-serif;
    position: relative;
  }
  .card {
    position: absolute;
    left: 284px;
    width: 598px;
    height: 364px;
    border-radius: 40px;
    overflow: hidden;
    box-shadow: 4px 6px 10px rgba(0,0,0,0.25);
  }
  .card--back { top: 142px; background: var(--card-dark); }
  .card--front { top: 544px; background: var(--card-light); }

  .brand {
    position: absolute;
    left: 149px;
    display: flex;
    align-items: center;
    gap: 14px;
  }
  .brand__mark {
    width: 64px; height: 64px;
    border-radius: 50%;
    border: 7px solid currentColor;
  }
  .brand__name {
    font-weight: 600;
    font-size: 31px;
    letter-spacing: 0.5px;
    line-height: 1;
  }
  .card--back .brand { top: 148px; color: var(--ink-faint); }
  .card--front .brand { top: 50px; color: var(--ink-dark); }

  .services {
    position: absolute;
    left: 30px; right: 30px; top: 293px;
    border-top: 1px solid var(--rule-dark);
    padding-top: 9px;
    text-align: center;
    color: var(--ink-faint);
    font-size: 14px;
    line-height: 18px;
  }

  .watermark {
    position: absolute;
    left: 258px; top: 2px;
    width: 340px; height: 340px;
    border-radius: 50%;
    border: 28px solid var(--watermark);
  }

  .person {
    position: absolute;
    right: 333px; top: 190px;
    text-align: right;
  }
  .person__name {
    color: var(--brand-red);
    font-weight: 700;
    font-size: 22px;
    line-height: 26px;
  }
  .person__title {
    color: var(--ink-muted);
    font-size: 17px;
    line-height: 22px;
  }
  .divider {
    position: absolute;
    left: 280px; top: 176px;
    width: 1px; height: 70px;
    background: var(--rule-light);
  }
  .contacts {
    position: absolute;
    left: 299px; top: 182px;
    list-style: none;
    color: var(--ink-muted);
    font-size: 16.5px;
    line-height: 21px;
  }
  .contacts li { display: flex; align-items: center; gap: 8px; }
  .contacts svg { width: 14px; height: 14px; fill: var(--brand-red); flex: none; }
</style>
</head>
<body>
  <section class="card card--back">
    <div class="brand">
      <span class="brand__mark"></span>
      <span class="brand__name">Harlow Ironworks LLC</span>
    </div>
    <p class="services">
      Welding and Demolition • Operation and Maintenance of industrial machinery<br>
      • Setting/moving and installation of industrial machinery
    </p>
  </section>

  <section class="card card--front">
    <div class="watermark"></div>
    <div class="brand">
      <span class="brand__mark"></span>
      <span class="brand__name">Harlow Ironworks LLC</span>
    </div>
    <div class="person">
      <p class="person__name">Name Surname</p>
      <p class="person__title">Title</p>
    </div>
    <div class="divider"></div>
    <ul class="contacts">
      <li>
        <svg viewBox="0 0 24 24" aria-hidden="true"><path d="M6.6 10.8a15.1 15.1 0 0 0 6.6 6.6l2.2-2.2a1 1 0 0 1 1-.25 11.4 11.4 0 0 0 3.6.57 1 1 0 0 1 1 1V20a1 1 0 0 1-1 1A17 17 0 0 1 3 4a1 1 0 0 1 1-1h3.5a1 1 0 0 1 1 1c0 1.25.2 2.45.57 3.57a1 1 0 0 1-.25 1z"/></svg>
        555-014-2290
      </li>
      <li>
        <svg viewBox="0 0 24 24" aria-hidden="true"><path d="M2 5h20v14H2z M4 7v.5l8 5.5 8-5.5V7l-8 5.5z" fill-rule="evenodd"/></svg>
        crew@harlowironworks.com
      </li>
      <li>
        <svg viewBox="0 0 24 24" aria-hidden="true"><path d="M12 2a10 10 0 1 0 0 20 10 10 0 0 0 0-20zm-1 2.1V8H7.6A8 8 0 0 1 11 4.1zm2 0A8 8 0 0 1 16.4 8H13zM6.5 10H11v4H6.5a8 8 0 0 1 0-4zm6.5 0h4.5a8 8 0 0 1 0 4H13zm-5.4 6H11v3.9A8 8 0 0 1 7.6 16zm5.4 0h3.4a8 8 0 0 1-3.4 3.9z"/></svg>
        harlowironworks.com
      </li>
    </ul>
  </section>
</body>
</html>
```